One pager fact sheet for healthcare companies

We are looking for a designer to create a theme based off this example. The project will consist of building a layout and theme for a one page, front and back handout. The handout will be used as part of an educational series for medical professionals. The format must be suitable for print production. The theme should be clear, concise, and professional. Cluttered graphics will not be useable.
This project has potential to include additional work over the next 3 months.

Target Market(s)

Healthcare professionals

Industry/Entity Type

Healthcare

Font styles to use
Serif
Sans Serif

Requirements
Must have
• A professional look and feel
Should not have
• Cluttered graphics or busy look

```html
<!DOCTYPE html>
<html lang="en">
<head>
<meta charset="utf-8">
<title>Health System Fact Sheet</title>
<link href="https://fonts.googleapis.com/css2?family=Open+Sans:wght@400;600;700&display=swap" rel="stylesheet">
<style>
:root{
  --bg:#e9e7e3;
  --paper:#ffffff;
  --header:#eceef0;
  --navy:#2c4c6e;
  --heading:#4a86c4;
  --rule:#4e6783;
  --text:#222;
  --footer:#6d9bd1;
}
*{box-sizing:border-box;margin:0;padding:0}
html,body{width:1200px;height:864px;overflow:hidden;background:var(--bg);font-family:"Open Sans",Arial,sans-serif;color:var(--text)}
.sheet{position:absolute;width:518px;height:669px;background:var(--paper);box-shadow:0 4px 14px rgba(0,0,0,.18);overflow:hidden}
.sheet.front{left:90px;top:74px}
.sheet.back{left:622px;top:108px}
.abs{position:absolute}
.header-band{left:0;top:0;width:518px;height:81px;background:var(--header)}
.contact-fields{left:258px;top:14px;font-size:10.5px;color:var(--navy);line-height:12.8px}
.contact-fields .row{display:flex;align-items:flex-end}
.contact-fields .lbl{width:60px}
.contact-fields .line{width:170px;border-bottom:1px solid var(--navy);height:10px;margin-left:6px}
.tab{background:var(--navy);width:29px;border-top-right-radius:9px;display:flex;flex-direction:column;justify-content:flex-end;align-items:center;padding-bottom:8px}
.tab span{writing-mode:vertical-rl;transform:rotate(180deg);color:#fff;font-weight:700;font-size:13.5px;white-space:nowrap;line-height:1.05;text-align:left}
.tab.small span{font-size:9px}
.tab.mid span{font-size:12.5px}
h3{font-weight:400;color:var(--heading);font-size:10.4px;line-height:11px}
.body{font-size:7.8px;line-height:11px}
.body.tight{font-size:7.4px;line-height:10.9px}
ul{list-style:none}
ul li{position:relative;padding-left:14px}
ul li::before{content:"•";position:absolute;left:2px}
.rule{height:0;border-top:1.2px solid var(--rule)}
.footer-band{left:0;top:638px;width:518px;height:31px;background:var(--footer);color:#e8f0fa;font-size:6.6px;padding:10px 0 0 28px}
.back .footer-band{padding-left:33px}
.dist li{display:flex;justify-content:space-between;width:170px}
.plans{display:grid;grid-template-columns:100px 100px;font-size:8.2px;line-height:11px}
.opt{display:inline-flex;align-items:flex-end;font-size:7.8px}
.blank{display:inline-block;width:19px;border-bottom:1px solid #333;text-align:center;line-height:9px;margin-right:4px;font-size:8px}
.opts{display:grid;font-size:7.8px;line-height:11px}
.para{font-size:7.6px;line-height:11px;width:434px}
.para.narrow{font-size:7.1px;line-height:10.9px;width:432px}
</style>
</head>
<body>

<section class="sheet front">
  <div class="abs header-band"></div>
  <div class="abs contact-fields">
    <div class="row"><span class="lbl">Name</span>:<span class="line"></span></div>
    <div class="row"><span class="lbl">Address</span>:<span class="line"></span></div>
    <div class="row"><span class="lbl">Address</span>:<span class="line"></span></div>
    <div class="row"><span class="lbl">Website</span>:<span class="line"></span></div>
  </div>

  <div class="abs tab" style="left:0;top:97px;height:209px"><span>Key Facts</span></div>
  <div class="abs tab mid" style="left:260px;top:97px;height:209px"><span>System Structure</span></div>

  <!-- Key facts column -->
  <h3 class="abs" style="left:42px;top:105px">Organization Type :</h3>
  <div class="abs body" style="left:53px;top:116px;font-size:8.2px">Not for Profit Health System</div>
  <div class="abs rule" style="left:42px;top:128px;width:197px"></div>
  <h3 class="abs" style="left:42px;top:133px;width:200px">Leadership Team and Contact Information:</h3>
  <div class="abs rule" style="left:42px;top:156px;width:197px"></div>
  <ul class="abs body" style="left:50px;top:159px;width:190px;font-size:8.2px">
    <li>Helen R. Whitcomb, CEO</li>
    <li>Marcus D. Ellery, III, President</li>
    <li>Thomas J. Varnell, EVP and COO</li>
    <li>Samuel Okafor, Jr. MD, EVP and Chief Medical Officer</li>
  </ul>
  <div class="abs rule" style="left:42px;top:216px;width:197px"></div>
  <h3 class="abs" style="left:42px;top:221px">Physicians in Network</h3>
  <ul class="abs body tight" style="left:50px;top:234px;width:190px">
    <li>Total&nbsp; :2,400 Salaried, 3,000 Affiliated</li>
    <li>PCPs&nbsp; :1,000 Salaried, 1,500 Affiliated</li>
    <li>Ophthalmologists&nbsp; : 35 Salaried, 0 Affiliated</li>
    <li>Retina Specialists&nbsp; : 10 Salaried, 0 Affiliated</li>
  </ul>
  <div class="abs rule" style="left:42px;top:283px;width:197px"></div>
  <h3 class="abs" style="left:42px;top:286px">Covered Lives</h3>
  <div class="abs body" style="left:206px;top:286px;font-size:8.2px">800,000</div>

  <!-- System structure column -->
  <h3 class="abs" style="left:302px;top:105px">Geographic Coverage&nbsp; :</h3>
  <div class="abs body" style="left:303px;top:116px;font-size:8.2px">Michigan</div>
  <div class="abs rule" style="left:302px;top:128px;width:197px"></div>
  <h3 class="abs" style="left:302px;top:133px">Number of Hospitals and Facilities:</h3>
  <ul class="abs body" style="left:302px;top:146px;width:190px;font-size:8.2px">
    <li>7 Hospitals</li>
    <li>Over 35 medical centers and facilities across multiple counties in Michigan</li>
  </ul>
  <div class="abs rule" style="left:302px;top:186px;width:197px"></div>
  <h3 class="abs" style="left:302px;top:192px">Key Affiliations</h3>
  <ul class="abs body tight" style="left:302px;top:207px;width:180px">
    <li>Medical Group has more than 1,100 physicians that staff CG hospital, West Lakeview hospital, and 26 medical centers</li>
    <li>Physician Network is a physician- led subsidiary, comprising the Medical Group, hospital-employed and private practice physicians</li>
    <li>2,000 affiliated private practice physicians</li>
  </ul>
  <div class="abs rule" style="left:260px;top:306px;width:239px"></div>

  <!-- Services -->
  <div class="abs tab" style="left:0;top:328px;height:90px"><span>Services</span></div>
  <h3 class="abs" style="left:42px;top:333px">Key Services and Facilities</h3>
  <ul class="abs body tight" style="left:50px;top:352px;width:186px">
    <li>Major service lines: cardiac care, women’s and children’s services, cancer care, orthopedics, transplants, neuroscience, trauma, and urology</li>
    <li>Key Facilities: ClearView centers include offices for ophthalmologists and retina specialists</li>
  </ul>
  <h3 class="abs" style="left:303px;top:329px">Distribution of Outpatient Services</h3>
  <ul class="abs body dist" style="left:302px;top:354px;font-size:8.2px">
    <li><span>In Facilities:</span><span>40%</span></li>
    <li><span>In Owned Practices:</span><span>30%</span></li>
    <li><span>In Affiliated Practices:</span><span>20%</span></li>
    <li><span>Unaffiliated/ Out of Network:</span><span>10%</span></li>
  </ul>
  <div class="abs rule" style="left:0;top:418px;width:499px"></div>

  <!-- Payers -->
  <div class="abs tab small" style="left:0;top:440px;height:198px"><span>Key Payer Relationships and<br>Payment Models</span></div>
  <h3 class="abs" style="left:42px;top:441px">Key Plans:</h3>
  <div class="abs plans" style="left:42px;top:460px">
    <span>Northline</span><span>Medicare</span>
    <span>Lakeshore Blue</span><span>Michigan Medicaid</span>
    <span>BlueHarbor Network</span><span>Morena</span>
    <span>Humeris</span><span>Primacy Health</span>
    <span>Carlow Health</span><span>Unity Healthcare</span>
  </div>
  <h3 class="abs" style="left:303px;top:445px">Level of Risk Taken</h3>
  <ul class="abs body" style="left:302px;top:464px;width:170px;font-size:8.2px">
    <li>80% of revenue is billed under a risk-based payment scheme</li>
    <li>Half of these lives include the risk for outpatient, physician- administered biologics</li>
  </ul>
  <div class="abs rule" style="left:42px;top:528px;width:457px"></div>
  <ul class="abs body tight" style="left:48px;top:541px;width:448px">
    <li>COMPANY accepts a variety of risk-based payment models including full and partial risk, bundled payments, and ACO contracts.</li>
    <li>All decisions to join an ACO or participate in a risk-based contract are made at the corporate level.</li>
    <li>COMPANY is contracted with CMS as a Next Generation ACO. Through the HMO product, this contract represents 30% of the health system’s revenue and covers over 20,000 Medicare lives.</li>
    <li>The remaining share of revenue typically includes a value-based payment model. Contracts with private payers, such as Lakeshore Blue, incorporate contracts based on performance and quality of care which may lead to bonus payments.</li>
  </ul>

  <div class="abs footer-band">Source: www.organization.example website pages. Perceva web survey conducted November 2016.</div>
</section>

<section class="sheet back">
  <div class="abs tab small" style="left:0;top:44px;height:172px"><span>Retina Specialist Reimbursement</span></div>
  <h3 class="abs" style="left:42px;top:45px">Dominant Reimbursement Models Used:</h3>
  <div class="abs opts" style="left:44px;top:58px;grid-template-columns:148px 148px 100px">
    <span class="opt"><span class="blank"></span>Fee for Service (FFS)</span>
    <span class="opt"><span class="blank"></span>Reduced FFS w/ withholding</span>
    <span class="opt"><span class="blank"></span>FFS with bonus</span>
    <span class="opt"><span class="blank">X</span>Salaried plus bonus</span>
    <span class="opt"><span class="blank"></span>Capitation</span>
  </div>
  <div class="abs rule" style="left:42px;top:93px;width:434px"></div>
  <h3 class="abs" style="left:44px;top:102px">Incentive Programs:</h3>
  <div class="abs opts" style="left:45px;top:119px;grid-template-columns:148px 148px">
    <span class="opt"><span class="blank">X</span>Bonus Pools</span>
    <span class="opt"><span class="blank"></span>Shared Savings</span>
  </div>
  <p class="abs para" style="left:42px;top:138px">Salaried retina specialists are eligible for bonus payments based on key performance metrics. Through Medora, the integrated electronic health record platform, data is collected on productivity metrics such as number of patients treated, drug costs, and quality of care. Quality metrics are specific to eye care as well as related to general patient care. Calculations for bonus payments are measured across the entire medical group and not individually by specialty. Exclusions may be made for outlier patient cases.</p>

  <div class="abs tab small" style="left:0;top:232px;height:124px"><span>Retina Specialist<br>Referrals</span></div>
  <h3 class="abs" style="left:42px;top:236px">Retina specialist network development</h3>
  <p class="abs para" style="left:46px;top:252px;width:430px">Health System is not pursuing acquisitions of retina specialist practices currently. The presence of academic institutions and teaching facilities ensures there is no shortage of retina specialists in the southern eastern portion of Michigan.</p>
  <h3 class="abs" style="left:42px;top:297px">Referral Process</h3>
  <p class="abs para" style="left:42px;top:315px">Health System leverages the EHR capabilities to facilitate in-network referrals. Primary care physicians can refer patients directly to retina specialist offices during the patient’s visit. Referrals among physicians are based on physician relationships, not directed to specific providers by the health system.</p>
  <div class="abs rule" style="left:42px;top:358px;width:434px"></div>

  <div class="abs tab" style="left:0;top:384px;height:254px"><span>Anti-VEGF Management</span></div>
  <h3 class="abs" style="left:49px;top:383px">Process Exists for Anti-VEGF Drug Management?</h3>
  <div class="abs opts" style="left:49px;top:400px;grid-template-columns:146px 146px 50px">
    <span class="opt"><span class="blank">X</span>Yes, for salaried physicians</span>
    <span class="opt"><span class="blank"></span>Yes, for affiliated physicians</span>
    <span class="opt"><span class="blank"></span>No</span>
  </div>
  <div class="abs rule" style="left:48px;top:418px;width:428px"></div>
  <h3 class="abs" style="left:49px;top:424px">Use of EHR system and Anti-VEGF Drugs</h3>
  <div class="abs opts" style="left:49px;top:445px;grid-template-columns:146px 146px 50px">
    <span class="opt"><span class="blank">X</span>Yes, for monitoring Rx</span>
    <span class="opt"><span class="blank"></span>Yes, for influencing Rx</span>
    <span class="opt"><span class="blank"></span>No</span>
  </div>
  <div class="abs rule" style="left:48px;top:462px;width:428px"></div>
  <h3 class="abs" style="left:49px;top:469px">Anti-VEGF Management Tools Utilized</h3>
  <div class="abs opts" style="left:46px;top:483px;grid-template-columns:147px 147px 140px;line-height:11px">
    <span class="opt"><span class="blank">X</span>Prescriber Education</span>
    <span class="opt"><span class="blank"></span>CPOE</span>
    <span class="opt"><span class="blank"></span>Centralized Formulary</span>
    <span class="opt"><span class="blank"></span>Preferred Product Lists</span>
    <span class="opt"><span class="blank"></span>Centralized Drug Supply</span>
    <span class="opt"><span class="blank"></span>Prior Authorizations</span>
    <span class="opt"><span class="blank"></span>Step Therapy</span>
    <span class="opt"><span class="blank"></span>Treatment Pathways</span>
    <span class="opt"><span class="blank"></span>Utilization Reports</span>
    <span class="opt"><span class="blank"></span>Consensus Building</span>
    <span class="opt"><span class="blank"></span>Newsletters</span>
    <span class="opt"><span class="blank"></span>Outlier Counseling</span>
  </div>
  <div class="abs para narrow" style="left:44px;top:538px">
    <p>Health System does not direct physician prescribing of anti-VEGF medications.</p>
    <p>HMO currently has a formulary with Vastorin and Lucevra preferred. Due to the Next Generation ACO contract adopting the HMO management policies, all ACO patients are subject to the health plan’s management. This includes prior authorizations, preferred products, and step therapy. HMO and ACO patients are required to try and fail either Vastorin or Lucevra before approval of Eyvara is attained.</p>
    <p>Patients covered under other payers must follow the criteria set forth by the patient’s health plan. If there is no preferred product or management tool indicated in the medical policy, retina specialists may prescribe their drug of choice without restriction from the health system.</p>
  </div>

  <div class="abs footer-band">Source: www.organization.example website pages. Perceva web survey conducted November 2016.</div>
</section>

</body>
</html>
```